Maplewood Farms - business cards
Business Card
Project: Maplewood Farms - business cards
Maplewood Farms - business cards - Agriculture
Creative Brief
Use same font as used in my logo
Glen Patters
38672 Red Falcon Lane Brookvale, OR 97555
gpatters@ironvale-partners.example
Can I see the design for a one sided card vs a 2 sided card? I want to send to the printer to see how much more it costs for 2 sided.
we might just do one sided; for a two sided card, just the logo

```html
<!DOCTYPE html>
<html lang="en">
<head>
<meta charset="utf-8">
<title>Maplewood Farms – Business Card</title>
<link rel="stylesheet" href="https://fonts.googleapis.com/css2?family=Carlito:wght@400;700&display=swap">
<style>
  :root {
    --backdrop: #1e1e1e;
    --card: #ffffff;
    --gold: #b8862b;
    --gold-line: #c99a3e;
    --ink: #3f3f3f;
  }
  * { margin: 0; padding: 0; box-sizing: border-box; }
  html, body {
    width: 1200px; height: 946px; overflow: hidden;
    background: var(--backdrop);
    font-family: "Carlito", "Calibri", sans-serif;
  }
  .card {
    position: absolute; left: 115px; top: 197px;
    width: 970px; height: 552px;
    background: var(--card);
    border-radius: 16px;
  }
  .brand {
    position: absolute; left: 44px; top: 100px;
    display: flex; align-items: center; gap: 14px;
    color: var(--gold);
    font-weight: 700; font-size: 46px; line-height: 52px;
    white-space: nowrap;
  }
  .brand-dot {
    width: 22px; height: 22px; border-radius: 50%;
    background: var(--gold); flex: none;
  }
  .divider {
    position: absolute; left: 0; right: 0; top: 284px;
    display: flex; align-items: center; gap: 12px;
  }
  .rule { height: 2px; background: var(--gold-line); }
  .rule-left { flex: 1; }
  .rule-right { width: 72px; flex: none; }
  .name {
    color: var(--gold);
    font-weight: 700; font-size: 38px; line-height: 44px;
    white-space: nowrap;
  }
  .contact {
    position: absolute; right: 31px; top: 392px;
    list-style: none;
    color: var(--ink); font-size: 25px; line-height: 34px;
    text-align: right;
  }
  .contact li {
    display: flex; align-items: center; justify-content: flex-end; gap: 12px;
    white-space: nowrap;
  }
  .contact svg { width: 24px; height: 24px; flex: none; }
</style>
</head>
<body>
  <div class="card">
    <div class="brand"><span class="brand-dot"></span>Maplewood Farms</div>

    <div class="divider">
      <div class="rule rule-left"></div>
      <div class="name">Glen Patters</div>
      <div class="rule rule-right"></div>
    </div>

    <ul class="contact">
      <li>509.555.0148
        <svg viewBox="0 0 24 24" aria-hidden="true">
          <rect x="6" y="2" width="12" height="20" rx="2" fill="var(--gold)"/>
          <rect x="8" y="5" width="8" height="10" fill="#fff"/>
          <circle cx="12" cy="18.5" r="1.3" fill="#fff"/>
        </svg>
      </li>
      <li>gpatters@ironvale-partners.example
        <svg viewBox="0 0 24 24" aria-hidden="true">
          <rect x="2" y="6" width="20" height="13" rx="1.5" fill="var(--gold)"/>
          <path d="M3 7 L12 14 L21 7" fill="none" stroke="#fff" stroke-width="1.6"/>
        </svg>
      </li>
      <li>38672 Red Falcon Lane Brookvale, OR 97555
        <svg viewBox="0 0 24 24" aria-hidden="true">
          <path d="M12 3 L2 12 H5 V21 H10 V15 H14 V21 H19 V12 H22 Z" fill="var(--gold)"/>
        </svg>
      </li>
    </ul>
  </div>
</body>
</html>
```